Healthcare Technology Company Business Card Design

Hi,

We require a new business card design thats catchy and professional.
Our target audience is healthcare professionals. See supplied artwork for our logo.

If you think its achievable please try add the tag line, not necessary however.
"Developing technologies to improve patient care and release operation benefits"

We'll require the following information on the card. No need to have the subject titles but i've referenced them for your convenience.

Personal Details
Paul Dwyer
Position: Director
Phone Number - 03 9472 5836
Mobile Number - 0438 275 904
Email: firstname.lastname@mediqbay.com.au

Company Details
Suite 31, 286 Keldon Street
Port Melbourne, Victoria
Fax: 03 8241 3975
mediqbay.com.au

Prefer a thinner design than the normal stock standard business card dimensions.
Please ensure there is adequate bleed.

Target Market(s)

Healthcare Professionals

Industry/Entity Type

Healthcare

Font styles to use
Sans Serif

Requirements
Must have
• Clean, Sharp Looks
Should not have
• Any healthcare symbols

```html
<!DOCTYPE html>
<html lang="en">
<head>
<meta charset="utf-8">
<title>mediqbay business card</title>
<link href="https://fonts.googleapis.com/css2?family=Source+Sans+3:wght@400;600;700&display=swap" rel="stylesheet">
<style>
  :root {
    --orange: #f29431;
    --blue: #2f6990;
    --navy: #244a60;
    --ink: #3a3a3a;
    --rule: #5b86a8;
    --page: #eceef2;
    --white: #ffffff;
  }
  * { box-sizing: border-box; margin: 0; padding: 0; }
  html, body {
    width: 1200px; height: 987px; overflow: hidden;
    background: var(--page);
    font-family: "Source Sans 3", Arial, sans-serif;
  }
  .canvas { position: relative; width: 1200px; height: 987px; }
  .card {
    position: absolute; left: 170px; width: 860px; height: 430px;
    border-radius: 28px; overflow: hidden;
    box-shadow: 0 6px 18px rgba(0,0,0,0.12);
  }
  .card--front { top: 45px; background: var(--white); }
  .card--back { top: 512px; background: var(--orange); }

  /* front */
  .brand { position: absolute; left: 52px; top: 38px; display: flex; align-items: center; gap: 14px; }
  .brand__mark { width: 46px; height: 46px; background: var(--orange); }
  .brand__name { font-size: 78px; font-weight: 700; color: var(--blue); line-height: 1; letter-spacing: -1px; }
  .person { position: absolute; left: 52px; top: 135px; font-size: 25px; }
  .person__name { color: var(--orange); font-weight: 700; }
  .person__role { color: var(--blue); font-weight: 400; }
  .contacts { position: absolute; left: 52px; top: 178px; font-size: 20px; color: var(--ink); line-height: 30px; }
  .contacts__row { display: flex; align-items: center; gap: 8px; }
  .contacts__gap { margin-left: 22px; }
  .icon { width: 16px; height: 16px; fill: var(--blue); flex: none; }
  .rule { position: absolute; left: 0; right: 0; height: 1px; background: var(--rule); }
  .rule--top { top: 296px; }
  .rule--bottom { top: 364px; }
  .band {
    position: absolute; left: 0; right: 0; top: 303px; height: 54px;
    background: var(--orange); display: flex; align-items: center; padding-left: 52px;
    font-size: 25px; color: var(--ink);
  }
  .address { position: absolute; left: 52px; top: 378px; font-size: 21px; color: var(--ink); }

  /* back */
  .back-brand {
    position: absolute; left: 0; right: 0; top: 110px; text-align: center;
    font-size: 120px; font-weight: 700; color: var(--white); line-height: 1; letter-spacing: -2px;
  }
  .tagline {
    position: absolute; left: 0; right: 0; top: 290px; text-align: center;
    font-size: 24px; font-weight: 600; color: var(--white); line-height: 1.25;
  }
</style>
</head>
<body>
<main class="canvas">
  <section class="card card--front">
    <div class="brand">
      <span class="brand__mark"></span>
      <span class="brand__name">mediqbay</span>
    </div>
    <p class="person"><span class="person__name">Paul Dwyer,</span> <span class="person__role">Director</span></p>
    <div class="contacts">
      <div class="contacts__row">
        <svg class="icon" viewBox="0 0 16 16"><path d="M4 1l3 3-2 2c1 2 3 4 5 5l2-2 3 3-2 3C7 15 1 9 1 3z"/></svg>
        <span>03 9472 5836</span>
        <svg class="icon contacts__gap" viewBox="0 0 16 16"><rect x="4" y="0" width="8" height="16" rx="1.5"/><rect x="5.5" y="2" width="5" height="7" fill="#fff"/></svg>
        <span>0438 275 904</span>
      </div>
      <div class="contacts__row">
        <svg class="icon" viewBox="0 0 16 16"><rect x="4" y="1" width="8" height="5"/><rect x="1" y="6" width="14" height="7" rx="1"/><rect x="4" y="10" width="8" height="5" fill="#fff" stroke="#2f6990"/></svg>
        <span>03 8241 3975</span>
      </div>
      <div class="contacts__row">
        <svg class="icon" viewBox="0 0 16 16"><rect x="1" y="3" width="14" height="10" rx="1"/><path d="M1 4l7 5 7-5" fill="none" stroke="#fff" stroke-width="1.5"/></svg>
        <span>firstname.lastname@mediqbay.com.au</span>
      </div>
    </div>
    <div class="rule rule--top"></div>
    <div class="band">www.mediqbay.com.au</div>
    <div class="rule rule--bottom"></div>
    <p class="address">Suite 31, 286 Keldon Street, Port Melbourne, Victoria</p>
  </section>

  <section class="card card--back">
    <p class="back-brand">mediqbay</p>
    <p class="tagline">Developing technologies to improve patient care<br>and release operation benefits</p>
  </section>
</main>
</body>
</html>
```